Healthcare and Professional IT Services Company need a redesigned business card

We are a IT Services company that targets small medical practices and professional business such as Attorneys, Accounts, Architects etc. We want to communicate a professional yet friendly image using recent logo redesign here on Sketchforge. Like to see the colors blue and orange in the design. Must use the Copper Lantern Technology as displayed in the new logo - then also want to incorporate the fish logo as well.

Target Market(s)

Small medical and professional services

Industry/Entity Type

It Company

Contact Information for Business Card

The usual stuff, place for name address phone website. Also maybe our tagline which is "hooked on technology"

Requirements
Must have
• My new logo and the fish somewhere on the card

```html
<!DOCTYPE html>
<html lang="en">
<head>
<meta charset="utf-8">
<title>Copper Lantern Technology – Business Card</title>
<link href="https://fonts.googleapis.com/css2?family=Source+Sans+3:wght@400;600;700&display=swap" rel="stylesheet">
<style>
  :root {
    --backdrop: #4a403b;
    --card: #0d0d0e;
    --card-edge: #1b1b1d;
    --brand-blue: #1e9ad6;
    --ink-light: #e8e8e8;
    --fish-orange: #ef7f3a;
    --fish-blue: #2f8fd0;
  }
  * { margin: 0; padding: 0; box-sizing: border-box; }
  html, body {
    width: 1200px; height: 900px; overflow: hidden;
    background: var(--backdrop);
    font-family: "Source Sans 3", "Myriad Pro", sans-serif;
  }
  .canvas {
    position: relative; width: 1200px; height: 900px;
    display: flex; align-items: center; justify-content: center; gap: 44px;
  }
  .card {
    position: relative; width: 540px; height: 310px;
    background: var(--card);
    border: 1px solid var(--card-edge);
    box-shadow: 0 14px 30px rgba(0,0,0,.45);
  }
  /* Front */
  .card-front { display: flex; }
  .brand-block {
    width: 260px; display: flex; flex-direction: column;
    align-items: center; justify-content: center; gap: 14px;
  }
  .brand-mark {
    width: 22px; height: 22px; border-radius: 50%;
    background: var(--brand-blue);
  }
  .brand-name {
    color: var(--brand-blue); font-weight: 700; font-size: 30px;
    line-height: 1.05; text-align: center; letter-spacing: -.3px;
  }
  .divider {
    width: 1px; margin: 40px 0;
    background: linear-gradient(to bottom, transparent, var(--brand-blue), transparent);
    opacity: .7;
  }
  .contact-block {
    flex: 1; padding: 52px 0 0 30px; color: var(--ink-light);
    font-size: 15px; line-height: 1.3;
  }
  .person-name { color: var(--brand-blue); font-weight: 700; font-size: 19px; }
  .person-title { margin-bottom: 16px; }
  .address { margin-bottom: 16px; }
  .contact-list { list-style: none; }
  .contact-list li { display: flex; align-items: center; gap: 9px; }
  .contact-list svg { width: 11px; height: 11px; fill: var(--brand-blue); flex: none; }
  /* Back */
  .card-back {
    display: flex; flex-direction: column; align-items: center; padding-top: 66px;
  }
  .fish-illustration {
    width: 150px; height: 86px; border-radius: 50%;
    background: radial-gradient(ellipse at 60% 50%, var(--fish-blue) 0%, var(--fish-blue) 45%, var(--fish-orange) 100%);
  }
  .tagline {
    margin-top: 44px; color: var(--brand-blue);
    font-weight: 700; font-size: 20px;
  }
</style>
</head>
<body>
<main class="canvas">
  <section class="card card-front">
    <div class="brand-block">
      <span class="brand-mark"></span>
      <div class="brand-name">Copper Lantern<br>Technology</div>
    </div>
    <div class="divider"></div>
    <div class="contact-block">
      <div class="person-name">Elliot Marsh</div>
      <div class="person-title">Managing Director</div>
      <div class="address">12345, Address Goes Here<br>Country Name, 123456.</div>
      <ul class="contact-list">
        <li><svg viewBox="0 0 12 12"><path d="M2 1h3l1 3-2 1a7 7 0 0 0 3 3l1-2 3 1v3c-6 0-9-3-9-9z"/></svg>044-555 018 274</li>
        <li><svg viewBox="0 0 12 12"><path d="M0 2h12v8H0zM1 3l5 4 5-4v-.2H1z"/></svg>info@copperlantern.net</li>
        <li><svg viewBox="0 0 12 12"><path d="M6 0a6 6 0 1 0 0 12A6 6 0 0 0 6 0zm0 1.5a4.5 4.5 0 1 1 0 9 4.5 4.5 0 0 1 0-9z"/></svg>www.copperlantern.net</li>
      </ul>
    </div>
  </section>
  <section class="card card-back">
    <div class="fish-illustration" role="img" aria-label="Cartoon fish illustration in blue and orange"></div>
    <p class="tagline">"hooked on technology"</p>
  </section>
</main>
</body>
</html>
```